Window Graphics for Chiropractic office

I need graphics design for my storefront windows for my chiropractic office. The city is very strict about how much of the windows can be covered. They don't allow for perforated decals at all. I will upload the specifics. The lettering and any graphics cannot occupy more than 20% of the windows. The lettering cannot be higher than 6 inches tall. The design that is need here will be submitted to a graphics design department where they design it on their software at the printing company. So it doesn't really matter here how clear the pics are etc. The design proofs I received from the printing company were very disappointing which is the reason I am requesting some designs from here. The door already has graphics on it that should match what is being designed on the window panes.
My office is spa, beachy like inside. I wouldn't mind something that exudes relaxation. I treat a lot of pregnant women and families as well as auto injuries.
Per the city, they state , "Window signs shall not exceed an aggregate area equal to 20 percent of the window on which they are located, or 9 square feet per window, whichever is less. Letter heights on window signs shall be a maximum of 6 inches."
Enclosed is the proof the printing company provided which I think is very blah. Maybe some color and small banners?
The left pane should read
Prenatal Chiropractic Care
Low Back Pain
Musculoskeletal Pelvic Pain
Sciatic Pain
Hip Pain
Children & Families
Wellness care
Sports injuries
Scoliosis
Musculoskeletal Pain
The middle Pane can be left as is in terms of what it says, except it should say call or text us at 555-208-7931
The right pane should say
Auto Injuries
Whiplash
Low Back Pain & Sciatica
Carpal Tunnel Syndrome
Plantar Fascitis/Achilles Tendinitis
Knee/Shoulder Pain
I'd like some feminine akin to what is attached with the Prenatal attachm,ent. The writing there might be too hard to read far away, but I like the gist of it. If it doesn't match the door that is no big deal. I can chage it if I really like the window pane design.

```html
<!DOCTYPE html>
<html lang="en">
<head>
<meta charset="utf-8">
<title>Seaview Chiropractic – Window Graphics</title>
<link href="https://fonts.googleapis.com/css2?family=Montserrat:ital,wght@0,400;0,500;0,600;0,700;1,600&family=Great+Vibes&display=swap" rel="stylesheet">
<style>
  :root {
    --backdrop: #f1e6e9;
    --frame: #3d3d3d;
    --pane: #ffffff;
    --ink: #333333;
    --blush: #ecd9e3;
    --blush-soft: rgba(222, 196, 214, 0.45);
    --lilac: #d9c3e4;
  }
  * { margin: 0; padding: 0; box-sizing: border-box; }
  html, body { width: 1200px; height: 717px; overflow: hidden; }
  body {
    background: var(--backdrop);
    font-family: "Montserrat", sans-serif;
    color: var(--ink);
    position: relative;
  }
  .storefront {
    position: absolute;
    left: 92px; top: 53px;
    width: 1003px; height: 603px;
    background: var(--frame);
  }
  .pane {
    position: absolute;
    background: var(--pane);
    overflow: hidden;
  }
  .pane--tall { top: 13px; height: 418px; width: 314px; }
  .pane--short { top: 446px; height: 142px; width: 314px; }
  .pane--left { left: 11px; }
  .pane--center { left: 344px; }
  .pane--right { left: 677px; }

  .wash {
    position: absolute;
    border-radius: 50%;
    background: radial-gradient(ellipse at center, var(--blush-soft) 0%, rgba(236,217,227,0.2) 55%, rgba(255,255,255,0) 75%);
  }
  .bloom {
    position: absolute;
    border-radius: 50%;
    background: radial-gradient(circle at 40% 40%, #f7f1f8 0%, var(--lilac) 60%, rgba(217,195,228,0) 100%);
  }

  .service-list {
    position: absolute;
    list-style: none;
    font-weight: 600;
    font-style: italic;
    font-size: 17.5px;
  }
  .service-list li {
    display: flex;
    align-items: center;
    white-space: nowrap;
  }
  .service-list li::before {
    content: "";
    width: 13px; height: 13px;
    border: 2px solid var(--ink);
    border-radius: 50%;
    margin-right: 10px;
    flex: none;
  }
  .service-list--left { left: 20px; top: 146px; }
  .service-list--left li { height: 23.5px; }
  .service-list--left li.group-start { margin-top: 24px; }
  .service-list--right { left: 20px; top: 144px; }
  .service-list--right li { height: 27.7px; }

  .brand-card { position: absolute; inset: 0; text-align: center; }
  .brand-mark {
    position: absolute; left: 117px; top: 66px;
    width: 80px; height: 80px;
    border: 7px solid var(--ink); border-radius: 50%;
  }
  .brand-name {
    position: absolute; left: 0; right: 0; top: 158px;
    font-size: 26px; font-weight: 700; letter-spacing: 0.5px; line-height: 1;
  }
  .brand-sub {
    position: absolute; left: 0; right: 0; top: 188px;
    font-size: 10.5px; font-weight: 500; letter-spacing: 3.6px;
  }
  .doctor {
    position: absolute; left: 0; right: 0; top: 206px;
    font-size: 20px; font-weight: 600;
  }
  .doctor-title {
    position: absolute; left: 0; right: 0; top: 232px;
    font-size: 15px; font-weight: 400;
  }
  .call-label {
    position: absolute; left: 0; right: 0; top: 264px;
    font-size: 25px; font-weight: 500;
  }
  .phone {
    position: absolute; left: 0; right: 0; top: 296px;
    font-size: 34px; font-weight: 700; letter-spacing: -0.5px;
  }
  .spanish {
    position: absolute; left: 0; right: 0; top: 343px;
    font-size: 17px; font-weight: 600;
  }

  .motto {
    position: absolute; left: 106px; top: 15px;
    width: 102px; height: 112px;
  }
  .motto-wreath {
    position: absolute; inset: 0;
    border-radius: 50%;
    background: radial-gradient(circle, rgba(255,255,255,0) 58%, rgba(80,80,80,0.18) 62%, rgba(80,80,80,0.08) 72%, rgba(255,255,255,0) 76%);
  }
  .motto-word {
    position: absolute; left: 0; right: 0; top: 36px;
    text-align: center;
    font-family: "Great Vibes", cursive;
    font-size: 27px; color: #222;
  }
</style>
</head>
<body>
  <div class="storefront">
    <!-- Left window pane -->
    <section class="pane pane--tall pane--left">
      <div class="wash" style="left:60px; top:180px; width:300px; height:260px;" role="img" aria-label="Soft pink watercolour wash"></div>
      <ul class="service-list service-list--left">
        <li>Prenatal Chiropractic Care</li>
        <li>Low Back Pain</li>
        <li>Musculoskeletal Pelvic Pain</li>
        <li>Sciatic Pain</li>
        <li>Hip Pain</li>
        <li class="group-start">Children &amp; Families</li>
        <li>Wellness care</li>
        <li>Sports injuries</li>
        <li>Scoliosis</li>
        <li>Musculoskeletal Pain</li>
      </ul>
    </section>

    <!-- Center window pane -->
    <section class="pane pane--tall pane--center">
      <div class="wash" style="left:120px; top:20px; width:260px; height:300px;" role="img" aria-label="Soft pink watercolour wash"></div>
      <div class="bloom" style="left:4px; top:-6px; width:60px; height:46px;" role="img" aria-label="Pale lilac flower illustration"></div>
      <div class="brand-card">
        <span class="brand-mark"></span>
        <div class="brand-name">SEAVIEW</div>
        <div class="brand-sub">CHIROPRACTIC</div>
        <div class="doctor">Dr. Maria Delgado, D.C.</div>
        <div class="doctor-title">Chiropractic Physician</div>
        <div class="call-label">Call us at</div>
        <div class="phone">555-208-7931</div>
        <div class="spanish">HABLAMOS ESPAÑOL</div>
      </div>
    </section>

    <!-- Right window pane -->
    <section class="pane pane--tall pane--right">
      <div class="wash" style="left:20px; top:-40px; width:320px; height:230px;" role="img" aria-label="Soft pink watercolour wash"></div>
      <div class="bloom" style="left:272px; top:130px; width:56px; height:76px;" role="img" aria-label="Pale lilac flower illustration"></div>
      <ul class="service-list service-list--right">
        <li>Auto Injuries</li>
        <li>Whiplash</li>
        <li>Low Back Pain &amp; Sciatica</li>
        <li>Carpal Tunnel Syndrome</li>
        <li>Plantar Fascitis/Achilles</li>
        <li>Tendinitis</li>
        <li>Knee/Shoulder Pain</li>
      </ul>
    </section>

    <!-- Bottom transom panes -->
    <section class="pane pane--short pane--left">
      <div class="wash" style="left:-20px; top:-30px; width:260px; height:180px;" role="img" aria-label="Soft pink watercolour wash"></div>
      <div class="bloom" style="left:-10px; top:62px; width:64px; height:86px;" role="img" aria-label="Pale lilac flower illustration"></div>
      <div class="motto">
        <div class="motto-wreath" role="img" aria-label="Leafy circular wreath ornament"></div>
        <div class="motto-word">Treat</div>
      </div>
    </section>
    <section class="pane pane--short pane--center">
      <div class="motto">
        <div class="motto-wreath" role="img" aria-label="Leafy circular wreath ornament"></div>
        <div class="motto-word">Revive</div>
      </div>
    </section>
    <section class="pane pane--short pane--right">
      <div class="bloom" style="left:252px; top:68px; width:70px; height:78px;" role="img" aria-label="Pale lilac flower illustration"></div>
      <div class="motto">
        <div class="motto-wreath" role="img" aria-label="Leafy circular wreath ornament"></div>
        <div class="motto-word">Heal</div>
      </div>
    </section>
  </div>
</body>
</html>
```